Varemo Group Business Card Design

The CEO is looking for a new trendy look for his business card.
You can stay with current branding or come up with something new/creative. It can be 3D, including Medical Office buildings. You can use our logo in a variety of colors. Please include name, title, company name, company website, email address, cell number

Target Market(s)

Real Estate Development and Construction

Industry/Entity Type

Health care real estate

Contact Information for Business Card

Rohesh Kumbar, CEO M-727.418.9062 E-roheshkumbar@varemo.com Address:4100 Lindell Ave, Tampa, FL 33611 www.varemo.com

Font styles to use
Other font styles liked:
• Be creative

Requirements
Must have
• Creative, trendy look
Nice to have
• Please go to our website to get a feel- www. varemo.com
Should not have
• small fonts

```html
<!DOCTYPE html>
<html lang="en">
<head>
<meta charset="utf-8">
<title>Varemo Group Business Card</title>
<link rel="stylesheet" href="https://fonts.googleapis.com/css2?family=Arimo:wght@400;700&display=swap">
<style>
  :root {
    --brand-red: #b51f2b;
    --brand-navy: #1f3260;
    --ink: #2a2f3a;
    --paper: #ffffff;
    --backdrop: #d9d9d9;
  }
  * { box-sizing: border-box; margin: 0; padding: 0; }
  html, body {
    width: 1200px; height: 788px; overflow: hidden;
    background: var(--backdrop);
    font-family: "Arimo", Arial, sans-serif;
  }
  .stage {
    width: 1200px; height: 788px;
    display: flex; align-items: center; justify-content: center; gap: 40px;
  }
  .card {
    position: relative;
    width: 540px; height: 309px;
    border-radius: 22px;
    overflow: hidden;
    box-shadow: 0 10px 26px rgba(0,0,0,.18);
  }
  /* Front */
  .card-front { background: var(--paper); }
  .front-wordmark {
    position: absolute; top: 34px; right: 38px;
    font-weight: 700; font-size: 40px; letter-spacing: -1px;
    color: var(--brand-red);
  }
  .holder { position: absolute; left: 38px; top: 118px; }
  .holder-name {
    font-weight: 700; font-size: 27px; color: var(--brand-red);
    letter-spacing: .5px; text-transform: uppercase;
  }
  .holder-title { font-size: 17px; color: var(--ink); margin-top: 2px; }
  .divider {
    position: absolute; left: 38px; right: 38px; top: 182px;
    height: 1px; background: var(--brand-navy);
  }
  .contact-list {
    position: absolute; left: 38px; top: 196px;
    list-style: none; font-size: 15px; color: var(--ink);
  }
  .contact-list li { display: flex; align-items: center; gap: 9px; line-height: 24px; }
  .contact-list svg { width: 13px; height: 13px; flex: none; }
  .address {
    position: absolute; right: 38px; top: 196px;
    font-size: 15px; line-height: 24px; color: var(--ink); text-align: right;
  }
  .edge-band { position: absolute; left: 0; bottom: 0; width: 540px; height: 16px; }
  /* Back */
  .card-back {
    background: var(--brand-navy);
    display: flex; align-items: center; justify-content: center;
  }
  .back-wordmark {
    font-weight: 700; font-size: 60px; letter-spacing: -1.5px;
    color: var(--paper);
  }
</style>
</head>
<body>
<main class="stage">
  <section class="card card-front" aria-label="Business card front">
    <div class="front-wordmark">Varemo Group</div>

    <div class="holder">
      <div class="holder-name">Rohesh Kumbar</div>
      <div class="holder-title">CEO</div>
    </div>

    <div class="divider"></div>

    <ul class="contact-list">
      <li>
        <svg viewBox="0 0 16 16" aria-hidden="true"><path fill="#b51f2b" d="M3.6 1.5l2.2 2.6-1.3 1.6c.9 2 2.4 3.6 4.4 4.6l1.6-1.3 2.6 2.2-1.5 2.3C6.2 13.2 2.6 9.5 1.4 3z"/></svg>
        727.418.9062
      </li>
      <li>
        <svg viewBox="0 0 16 16" aria-hidden="true"><rect x="1" y="3" width="14" height="10" rx="1.5" fill="#b51f2b"/><path d="M1.8 4l6.2 4.8L14.2 4" fill="none" stroke="#fff" stroke-width="1.3"/></svg>
        roheshkumbar@varemo.com
      </li>
      <li>
        <svg viewBox="0 0 16 16" aria-hidden="true"><circle cx="8" cy="8" r="7" fill="#b51f2b"/><path d="M1 8h14M8 1c-3 3.5-3 10.5 0 14M8 1c3 3.5 3 10.5 0 14" fill="none" stroke="#fff" stroke-width="1"/></svg>
        www.varemo.com
      </li>
    </ul>

    <div class="address">4100 Lindell Ave<br>Tampa, FL 33611</div>

    <svg class="edge-band" viewBox="0 0 540 16" preserveAspectRatio="none" aria-hidden="true">
      <polygon points="0,0 260,0 276,16 0,16" fill="var(--brand-red)"/>
      <polygon points="266,0 540,0 540,16 282,16" fill="var(--brand-navy)"/>
    </svg>
  </section>

  <section class="card card-back" aria-label="Business card back">
    <div class="back-wordmark">Varemo Group</div>
  </section>
</main>
</body>
</html>
```